Standard logo business card

We are seeking a solid, somewhat understated professional design. We are a tech company. We like fonts similar to Aptifer Slab. Front side will be white with the contact information and a small version of our primary (Light background) logo.

(We have three people so we will have three names and titles)

Back side will hold our reverse logo on dark background along with the tagline:

"Intelligent annotation solutions for complex data"

Target Market(s)

Professionals, Tech

Industry/Entity Type

Business

Contact Information for Business Card

Name
Title

Phone
Email
City, State
Website

[We will email leading designer specific contact information)

Font styles to use
Serif

Requirements
Must have
• Colors are:
• Orange RGB 245,92,23
• Blue RGB 3,34,56
Nice to have
• We like a split with the Name and Title on the right and then contact details (below) on the left.

```html
<!DOCTYPE html>
<html lang="en">
<head>
<meta charset="utf-8">
<title>Quantora Business Card</title>
<link href="https://fonts.googleapis.com/css2?family=Tinos:wght@400;700&display=swap" rel="stylesheet">
<style>
  :root {
    --orange: rgb(245, 92, 23);
    --blue: rgb(3, 34, 56);
    --white: #ffffff;
    --backdrop: #ece9e4;
  }
  * { margin: 0; padding: 0; box-sizing: border-box; }
  html, body {
    width: 1200px;
    height: 1037px;
    overflow: hidden;
    background: var(--backdrop);
    font-family: "Tinos", "Times New Roman", serif;
  }
  .canvas {
    position: relative;
    width: 1200px;
    height: 1037px;
  }
  .card {
    position: absolute;
    left: 260px;
    width: 680px;
    height: 390px;
    overflow: hidden;
    box-shadow: 0 6px 18px rgba(0, 0, 0, 0.18);
  }
  .card-front { top: 70px; background: var(--orange); }
  .card-back { top: 550px; background: var(--blue); }

  /* Front */
  .identity {
    position: absolute;
    left: 34px;
    top: 30px;
    color: var(--white);
  }
  .identity .name { font-size: 24px; line-height: 1.1; }
  .identity .title { font-size: 13px; margin-top: 2px; }
  .website {
    position: absolute;
    right: 70px;
    top: 78px;
    color: var(--white);
    font-size: 15px;
  }
  .contact {
    position: absolute;
    left: 34px;
    top: 150px;
    list-style: none;
    color: var(--white);
    font-size: 14px;
    line-height: 1.3;
  }
  .contact li {
    display: flex;
    align-items: flex-start;
    gap: 10px;
    margin-bottom: 4px;
  }
  .contact .icon { width: 14px; height: 16px; flex: none; margin-top: 1px; }
  .brand-band {
    position: absolute;
    left: 0;
    bottom: 0;
    width: 100%;
    height: 120px;
    background: var(--blue);
    display: flex;
    align-items: center;
    padding-left: 110px;
  }

  /* Brand wordmark */
  .brand {
    display: flex;
    align-items: center;
    gap: 16px;
  }
  .brand-mark {
    width: 42px;
    height: 42px;
    background: var(--orange);
  }
  .brand-name {
    color: var(--white);
    font-size: 62px;
    font-weight: 700;
    line-height: 1;
  }

  /* Back */
  .rule {
    position: absolute;
    left: 0;
    width: 100%;
    height: 4px;
    background: var(--white);
  }
  .rule-top { top: 16px; }
  .rule-upper { top: 108px; }
  .rule-lower { top: 330px; }
  .back-lockup {
    position: absolute;
    left: 0;
    top: 150px;
    width: 100%;
    display: flex;
    flex-direction: column;
    align-items: center;
  }
  .tagline {
    margin-top: 14px;
    color: var(--white);
    font-size: 21px;
    letter-spacing: 0.3px;
  }
</style>
</head>
<body>
<main class="canvas">

  <section class="card card-front" aria-label="Business card front">
    <div class="identity">
      <p class="name">Your Name</p>
      <p class="title">Title</p>
    </div>
    <p class="website">Your Website</p>

    <ul class="contact">
      <li>
        <svg class="icon" viewBox="0 0 14 16" aria-hidden="true">
          <path d="M7 1a5 5 0 0 1 5 5c0 3.5-5 9-5 9S2 9.5 2 6a5 5 0 0 1 5-5z" fill="#fff"/>
          <circle cx="7" cy="6" r="1.8" fill="rgb(245,92,23)"/>
        </svg>
        <span>Your City<br>Your State</span>
      </li>
      <li>
        <svg class="icon" viewBox="0 0 14 16" aria-hidden="true">
          <rect x="1" y="4" width="12" height="9" fill="#fff"/>
          <path d="M1 4l6 5 6-5" fill="none" stroke="rgb(245,92,23)" stroke-width="1.2"/>
        </svg>
        <span>Your Email.com</span>
      </li>
      <li>
        <svg class="icon" viewBox="0 0 14 16" aria-hidden="true">
          <rect x="3.5" y="1" width="7" height="14" rx="1.2" fill="none" stroke="#fff" stroke-width="1.2"/>
          <circle cx="7" cy="12.8" r="0.8" fill="#fff"/>
        </svg>
        <span>Your Phone Number</span>
      </li>
    </ul>

    <div class="brand-band">
      <div class="brand">
        <span class="brand-mark" aria-hidden="true"></span>
        <span class="brand-name">Quantora</span>
      </div>
    </div>
  </section>

  <section class="card card-back" aria-label="Business card back">
    <span class="rule rule-top"></span>
    <span class="rule rule-upper"></span>
    <div class="back-lockup">
      <div class="brand">
        <span class="brand-mark" aria-hidden="true"></span>
        <span class="brand-name">Quantora</span>
      </div>
      <p class="tagline">Intelligent annotation solutions for complex data</p>
    </div>
    <span class="rule rule-lower"></span>
  </section>

</main>
</body>
</html>
```